truck graphics

Would like graphic design for work truck advertising. The truck uploaded without graphics is the truck. The other with graphics is a concept idea.

Company name Brimfield Greenworks
731 482 5519
Use The name with the lines on top and bottom without the graphic

I like the green stripe of the truck but ours can say ‘Deeply Rooted In The Community’

On the bed of truck similar to picture
Lawn Care - Maintenance - Land Clearing - Bush Hogging

```html
<!DOCTYPE html>
<html lang="en">
<head>
<meta charset="utf-8">
<title>Brimfield Greenworks – Truck Graphics</title>
<link href="https://fonts.googleapis.com/css2?family=Poppins:wght@600;700;800&family=Oswald:wght@500;600&display=swap" rel="stylesheet">
<style>
  :root {
    --red: #e8453c;
    --navy: #25327a;
    --navy-deep: #1c2660;
    --white: #ffffff;
    --paper: #f4f4f2;
  }
  * { margin: 0; padding: 0; box-sizing: border-box; }
  html, body { width: 1200px; height: 1200px; overflow: hidden; }
  body { background: var(--white); font-family: "Poppins", sans-serif; position: relative; }

  .side-wrap, .rear-wrap, .hood-wrap {
    position: absolute;
    background: var(--paper);
    overflow: hidden;
  }
  .side-wrap { left: 200px; width: 600px; height: 140px; }
  .rear-wrap { left: 860px; width: 250px; height: 140px; }
  .hood-wrap { left: 900px; width: 170px; height: 60px; top: 820px; }

  .row-1 { top: 220px; }
  .row-2 { top: 500px; }
  .row-3 { top: 780px; }

  /* name block */
  .brand { position: absolute; text-align: center; }
  .brand-name {
    display: block;
    color: var(--red);
    font-weight: 800;
    text-transform: uppercase;
    line-height: 1.15;
    padding: 3px 0;
    border-top: 2px solid var(--navy);
    border-bottom: 2px solid var(--navy);
  }
  .phone {
    display: block;
    color: var(--navy);
    font-weight: 700;
    letter-spacing: 1px;
    margin-top: 4px;
    white-space: nowrap;
  }

  .side-wrap .brand { left: 16px; top: 28px; width: 190px; }
  .side-wrap .brand-name { font-size: 13px; white-space: nowrap; }
  .side-wrap .phone { font-size: 15px; }

  /* services */
  .services {
    position: absolute;
    font-family: "Oswald", sans-serif;
    font-weight: 500;
    color: var(--red);
    text-transform: uppercase;
    letter-spacing: 0.6px;
    text-align: right;
    white-space: nowrap;
  }
  .services .dot { color: var(--navy); margin: 0 4px; }
  .side-wrap .services { right: 16px; top: 12px; font-size: 12.5px; line-height: 1.45; }

  /* artwork placeholder */
  .scenery {
    position: absolute;
    background: linear-gradient(180deg, var(--red) 0%, var(--navy) 45%, var(--navy-deep) 100%);
  }
  .side-wrap .scenery { left: 215px; top: 10px; width: 170px; height: 87px; }
  .side-wrap .scenery.tail { left: 522px; top: 54px; width: 62px; height: 43px; }

  /* stripe */
  .stripe {
    position: absolute;
    left: 0; right: 0;
    background: var(--navy);
    color: var(--white);
    font-family: "Oswald", sans-serif;
    font-weight: 600;
    text-transform: uppercase;
    letter-spacing: 1px;
    display: flex;
    align-items: center;
    border-top: 3px solid var(--red);
    white-space: nowrap;
  }
  .side-wrap .stripe {
    bottom: 14px; height: 26px; font-size: 11.5px;
    padding-left: 40px;
    clip-path: polygon(3% 0, 100% 0, 100% 100%, 0 100%);
  }
  .side-wrap .stripe-text { width: 240px; text-align: center; }

  /* rear */
  .rear-wrap .brand { left: 12px; top: 20px; width: 110px; }
  .rear-wrap .brand-name { font-size: 10px; border-width: 1.5px; }
  .rear-wrap .phone { font-size: 10.5px; }
  .rear-wrap .scenery { left: 132px; top: 16px; width: 104px; height: 68px; }
  .rear-wrap .stripe {
    bottom: 26px; height: 22px; font-size: 9.5px;
    justify-content: center;
  }
  .row-2.rear-wrap .scenery { left: 14px; top: 10px; width: 70px; height: 32px; }
  .row-2.rear-wrap .brand { top: 46px; }
  .row-2.rear-wrap .services { right: 14px; top: 12px; font-size: 9px; line-height: 1.35; }
  .row-2.rear-wrap .phone { position: absolute; left: 128px; top: 72px; font-size: 11px; margin: 0; }

  /* hood */
  .hood-wrap .scenery { left: 55px; top: 4px; width: 60px; height: 24px; }
  .hood-wrap .brand { left: 12px; top: 31px; width: 146px; }
  .hood-wrap .brand-name { font-size: 9.5px; border-width: 1.5px; padding: 1px 0; white-space: nowrap; }
</style>
</head>
<body>

  <section class="side-wrap row-1">
    <div class="brand">
      <span class="brand-name">Brimfield Greenworks</span>
      <span class="phone">731 482 5519</span>
    </div>
    <div class="scenery" role="img" aria-label="Setting sun over navy mountains with a winding road and pine trees"></div>
    <p class="services">Lawn Care<span class="dot">•</span>Maintenance<br>Land Clearing<span class="dot">•</span>Bush Hogging</p>
    <div class="stripe"><span class="stripe-text">Deeply Rooted In The Community</span></div>
  </section>

  <section class="rear-wrap row-1">
    <div class="brand">
      <span class="brand-name">Brimfield Greenworks</span>
      <span class="phone">731 482 5519</span>
    </div>
    <div class="scenery" role="img" aria-label="Setting sun over navy mountains with a winding road and pine trees"></div>
    <div class="stripe">Deeply Rooted In The Community</div>
  </section>

  <section class="side-wrap row-2">
    <div class="brand">
      <span class="brand-name">Brimfield Greenworks</span>
      <span class="phone">731 482 5519</span>
    </div>
    <div class="scenery" role="img" aria-label="Setting sun over navy mountains with a winding road and pine trees"></div>
    <p class="services">Lawn Care<span class="dot">•</span>Maintenance<br>Land Clearing<span class="dot">•</span>Bush Hogging</p>
    <div class="stripe"><span class="stripe-text">Deeply Rooted In The Community</span></div>
  </section>

  <section class="rear-wrap row-2">
    <div class="scenery" role="img" aria-label="Small sun and mountain scene"></div>
    <div class="brand">
      <span class="brand-name">Brimfield Greenworks</span>
    </div>
    <p class="services">Lawn Care •<br>Maintenance •<br>Land Clearing •<br>Bush Hogging •</p>
    <span class="phone">731 482 5519</span>
    <div class="stripe">Deeply Rooted In The Community</div>
  </section>

  <section class="side-wrap row-3">
    <div class="brand">
      <span class="brand-name">Brimfield Greenworks</span>
      <span class="phone">731 482 5519</span>
    </div>
    <div class="scenery" role="img" aria-label="Setting sun over navy mountains with a winding road and pine trees"></div>
    <p class="services">Lawn Care<span class="dot">•</span>Maintenance<br>Land Clearing<span class="dot">•</span>Bush Hogging</p>
    <div class="scenery tail" role="img" aria-label="Navy mountain peak with pine trees on the rear of the bed"></div>
    <div class="stripe"><span class="stripe-text">Deeply Rooted In The Community</span></div>
  </section>

  <section class="hood-wrap">
    <div class="scenery" role="img" aria-label="Small sun and mountain scene"></div>
    <div class="brand">
      <span class="brand-name">Brimfield Greenworks</span>
    </div>
  </section>

</body>
</html>
```